Business Card Design Project - Harbourline Removals

I need a business card design created for my furniture removal business. The name is Harbourline Removals so something associated with the galaxy would be great ( possibly the southern cross or something to that effect). Modern, creative and simple was what I had in mind. I like metallic silver and different shades of blue but am open to other colour ideas.

Industry/Entity Type

Business

Requirements
Must have
• Something associated with the galaxy
Nice to have
• Have checked out lots of different fontstyles and really like 'kefa'

```html
<!DOCTYPE html>
<html lang="en">
<head>
<meta charset="utf-8">
<title>Harbourline Removals – Business Card</title>
<link rel="stylesheet" href="https://fonts.googleapis.com/css2?family=Andika:wght@400;700&display=swap">
<style>
  :root {
    --space-black: #010608;
    --deep-teal: #06303d;
    --mid-teal: #0f6b80;
    --glow-cyan: #19c4ea;
    --glow-core: #eafcff;
    --ink: #000000;
    --white: #ffffff;
    --tag-blue: #1462b4;
    --star: #ffffff;
  }
  html, body {
    margin: 0;
    padding: 0;
    width: 1200px;
    height: 686px;
    overflow: hidden;
    background: var(--space-black);
  }
  .card {
    position: relative;
    width: 1200px;
    height: 686px;
    overflow: hidden;
    font-family: "Andika", "Trebuchet MS", sans-serif;
    background:
      radial-gradient(ellipse 210px 130px at 590px 330px, var(--glow-core) 0%, rgba(160,240,255,0.85) 35%, rgba(25,196,234,0) 100%),
      radial-gradient(ellipse 470px 260px at 590px 320px, var(--glow-cyan) 0%, var(--mid-teal) 45%, rgba(6,48,61,0) 100%),
      radial-gradient(ellipse 760px 520px at 590px 320px, var(--deep-teal) 0%, #041c24 60%, var(--space-black) 100%);
  }
  .stars {
    position: absolute;
    inset: 0;
  }
  .card-text {
    position: absolute;
    left: 0;
    right: 0;
    text-align: center;
    margin: 0;
    white-space: nowrap;
  }
  .business-name {
    top: 160px;
    font-size: 88px;
    font-weight: 400;
    color: var(--white);
    letter-spacing: 1px;
    text-shadow:
      -2px -2px 0 var(--ink), 2px -2px 0 var(--ink), -2px 2px 0 var(--ink), 2px 2px 0 var(--ink),
      0 -2px 0 var(--ink), 0 2px 0 var(--ink), -2px 0 0 var(--ink), 2px 0 0 var(--ink),
      22px -14px 10px rgba(0,0,0,0.75);
  }
  .tagline {
    top: 290px;
    font-size: 48px;
    font-weight: 700;
    color: var(--tag-blue);
    letter-spacing: 1.5px;
    text-shadow:
      -1px -1px 0 #0a2540, 1px -1px 0 #0a2540, -1px 1px 0 #0a2540, 1px 1px 0 #0a2540,
      4px 4px 4px rgba(0,0,0,0.6);
  }
  .phone {
    top: 360px;
    font-size: 46px;
    font-weight: 700;
    color: var(--white);
    letter-spacing: 1px;
    text-shadow: 3px 3px 2px rgba(0,0,0,0.85), -1px -1px 0 rgba(0,0,0,0.5);
  }
  .website {
    top: 432px;
    font-size: 42px;
    font-weight: 700;
    color: var(--white);
    letter-spacing: 1px;
    text-shadow: 3px 3px 2px rgba(0,0,0,0.85), -1px -1px 0 rgba(0,0,0,0.5);
  }
</style>
</head>
<body>
  <main class="card">
    <svg class="stars" width="1200" height="686" viewBox="0 0 1200 686" aria-hidden="true">
      <defs>
        <radialGradient id="star-glow">
          <stop offset="0" stop-color="#ffffff" stop-opacity="1"/>
          <stop offset="1" stop-color="#ffffff" stop-opacity="0"/>
        </radialGradient>
        <g id="sparkle">
          <circle r="6" fill="url(#star-glow)"/>
          <path d="M0 -7 L1 -1 L7 0 L1 1 L0 7 L-1 1 L-7 0 L-1 -1 Z" fill="var(--star)"/>
        </g>
      </defs>
      <use href="#sparkle" x="355" y="95"/>
      <use href="#sparkle" x="448" y="100" transform="translate(448 100) scale(0.5) translate(-448 -100)"/>
      <use href="#sparkle" x="680" y="178"/>
      <use href="#sparkle" x="808" y="121" transform="translate(808 121) scale(0.6) translate(-808 -121)"/>
      <use href="#sparkle" x="1005" y="173"/>
      <use href="#sparkle" x="1105" y="62" transform="translate(1105 62) scale(0.7) translate(-1105 -62)"/>
      <use href="#sparkle" x="333" y="432"/>
      <use href="#sparkle" x="210" y="488" transform="translate(210 488) scale(0.6) translate(-210 -488)"/>
      <use href="#sparkle" x="868" y="435" transform="translate(868 435) scale(0.6) translate(-868 -435)"/>
      <use href="#sparkle" x="982" y="320" transform="translate(982 320) scale(0.6) translate(-982 -320)"/>
      <use href="#sparkle" x="140" y="318" transform="translate(140 318) scale(0.5) translate(-140 -318)"/>
      <use href="#sparkle" x="342" y="640" transform="translate(342 640) scale(0.6) translate(-342 -640)"/>
      <use href="#sparkle" x="452" y="632"/>
      <use href="#sparkle" x="795" y="546" transform="translate(795 546) scale(0.6) translate(-795 -546)"/>
      <use href="#sparkle" x="1053" y="572"/>
      <use href="#sparkle" x="1033" y="622" transform="translate(1033 622) scale(0.5) translate(-1033 -622)"/>
      <use href="#sparkle" x="1148" y="395" transform="translate(1148 395) scale(0.5) translate(-1148 -395)"/>
    </svg>

    <h1 class="card-text business-name">Harbourline Removals</h1>
    <p class="card-text tagline">Furniture moving company</p>
    <p class="card-text phone">Phone: 0487163205</p>
    <p class="card-text website">www.harbourlineremovals.com.au</p>
  </main>
</body>
</html>
```